Industrial Professional Business Card Design (Vantrel Systems)

Would like professional looking business cards. Not too busy leaning towards minimal. Should have a slogan like:
"Industrial Automation and Control".

We are a tech company that programs industrial PLC computers. We also develop custom hardware solutions. Please use the logo for inspiration.

Target Market(s)

Mining, industrial, processing, automation, factory

Industry/Entity Type

Engineering

Contact Information for Business Card

Name, phone, email, website. job title.

Font styles to use
Other font styles liked:
• droid sans

Requirements
Must have
• Use colours that go well with the logo. Not too busy design.

```html
<!DOCTYPE html>
<html lang="en">
<head>
<meta charset="utf-8">
<title>Vantrel Systems – Business Card</title>
<link href="https://fonts.googleapis.com/css2?family=Poppins:wght@400;500;600&display=swap" rel="stylesheet">
<style>
  :root {
    --navy: #1d2a5c;
    --navy-mid: #1f4a73;
    --blue-text: #1f4872;
    --orange: #f26b21;
    --grey-text: #4a4a4a;
    --rule: #555555;
    --card: #ffffff;
    --backdrop: #e4e4e4;
  }
  * { margin: 0; padding: 0; box-sizing: border-box; }
  html, body {
    width: 1125px; height: 1200px; overflow: hidden;
    background: var(--backdrop);
    font-family: "Poppins", sans-serif;
  }
  .canvas { position: relative; width: 1125px; height: 1200px; }

  .card { position: absolute; left: 150px; width: 826px; height: 471px; }
  .card--front { top: 98px; background: var(--card); }
  .card--back {
    top: 631px;
    background: radial-gradient(ellipse at 50% 45%, #21507a 0%, #1f3f6c 40%, var(--navy) 100%);
  }

  .brand {
    position: absolute; display: flex; align-items: center; gap: 14px;
    font-weight: 500; white-space: nowrap;
  }
  .brand__dot { border-radius: 50%; background: var(--orange); flex: none; }
  .card--front .brand { right: 45px; top: 250px; font-size: 38px; color: var(--blue-text); }
  .card--front .brand__dot { width: 30px; height: 30px; }
  .card--back .brand {
    left: 0; right: 0; top: 200px; justify-content: center;
    font-size: 46px; color: #ffffff;
  }
  .card--back .brand__dot { width: 36px; height: 36px; }

  .person { position: absolute; left: 42px; top: 290px; }
  .person__name { font-size: 27px; font-weight: 600; color: var(--blue-text); line-height: 1.2; }
  .person__title { font-size: 19px; font-weight: 400; color: var(--orange); line-height: 1.3; }

  .divider { position: absolute; left: 42px; right: 44px; top: 359px; height: 1px; background: var(--rule); }

  .contacts { position: absolute; left: 42px; top: 378px; list-style: none; }
  .contacts li {
    display: flex; align-items: center; gap: 11px;
    font-size: 19px; color: var(--grey-text); line-height: 25px;
  }
  .contacts svg { width: 15px; height: 15px; fill: var(--blue-text); flex: none; }

  .website {
    position: absolute; right: 44px; top: 403px;
    font-size: 19px; font-weight: 600; color: var(--blue-text);
  }

  .edge-band { position: absolute; left: 0; bottom: 0; width: 826px; height: 14px; }

  .slogan {
    position: absolute; left: 0; right: 0; top: 402px; text-align: center;
    font-size: 19px; font-weight: 500; color: #ffffff;
  }
  .slogan__accent { color: var(--orange); }
</style>
</head>
<body>
<main class="canvas">

  <section class="card card--front" aria-label="Business card front">
    <div class="brand"><span class="brand__dot"></span>Vantrel Systems</div>

    <div class="person">
      <p class="person__name">Daniel Hartley</p>
      <p class="person__title">President</p>
    </div>

    <div class="divider"></div>

    <ul class="contacts">
      <li>
        <svg viewBox="0 0 24 24" aria-hidden="true"><path d="M6.6 10.8a15.1 15.1 0 0 0 6.6 6.6l2.2-2.2c.3-.3.7-.4 1-.2 1.1.4 2.3.6 3.6.6.6 0 1 .4 1 1V20c0 .6-.4 1-1 1A17 17 0 0 1 3 4c0-.6.4-1 1-1h3.5c.6 0 1 .4 1 1 0 1.3.2 2.5.6 3.6.1.3 0 .7-.2 1z"/></svg>
        555-014-2287
      </li>
      <li>
        <svg viewBox="0 0 24 24" aria-hidden="true"><path d="M2 6h20v12H2z M2 6l10 7 10-7" fill="var(--blue-text)"/><path d="M3 7l9 6.3L21 7" fill="none" stroke="#fff" stroke-width="1.6"/></svg>
        info@vantrelsystems.com
      </li>
    </ul>

    <p class="website">www.vantrelsystems.com</p>

    <svg class="edge-band" viewBox="0 0 826 14" preserveAspectRatio="none" aria-hidden="true">
      <defs>
        <linearGradient id="band-blue" x1="0" x2="1" y1="0" y2="0">
          <stop offset="0" stop-color="#1a2455"/>
          <stop offset="0.5" stop-color="#21598a"/>
          <stop offset="1" stop-color="#1a2455"/>
        </linearGradient>
      </defs>
      <polygon points="0,0 538,0 534,14 0,14" fill="url(#band-blue)"/>
      <polygon points="544,0 826,0 826,14 540,14" fill="var(--orange)"/>
    </svg>
  </section>

  <section class="card card--back" aria-label="Business card back">
    <div class="brand"><span class="brand__dot"></span>Vantrel Systems</div>
    <p class="slogan">Industrial Automation <span class="slogan__accent">&amp; Control</span></p>
  </section>

</main>
</body>
</html>
```